K & M Tire Shop business cards

need business card for tire/car care company based in tampa, florida. we sell used and new tires, also we service vehicles, tune ups, oil chasnge, brakes and A/c we offer free towing with major vehicle repair and tire purchase. we also offer free estimates on any engine or a/c repair. also we have the lowest price in the city on used and new tires.

Industry/Entity Type

Business

Contact Information for Business Card

4187 N Crestwell Ave,
Tampa, Fl 33829
Ph: 813-572-6148
KandMTireShop@examplemail.com

Font styles to use
Serif
Sans Serif
Decorative

Requirements
Must have
• my logo, what we do ( used and new tires , oil change, brakes, tune ups, free towing vehicl. Also business info.
Nice to have
• an image of a towing truck, highlighting that we offer free towing. something close to what i have in one of the attached image

```html
<!DOCTYPE html>
<html lang="en">
<head>
<meta charset="utf-8">
<title>K &amp; M Tire Shop – Business Cards</title>
<link href="https://fonts.googleapis.com/css2?family=Lato:wght@400;700;900&family=Cinzel:wght@500&display=swap" rel="stylesheet">
<style>
  :root {
    --stage: #2b2b2b;
    --card: #f7f7f7;
    --card-edge: #e4e4e4;
    --ink: #1a1a1a;
    --ink-soft: #333333;
    --band-dark: #3c4452;
    --band-mid: #8a93a3;
    --band-light: #c9ced8;
    --accent: #e6de2a;
    --rule: #111111;
  }
  * { box-sizing: border-box; margin: 0; padding: 0; }
  html, body { width: 1200px; height: 873px; overflow: hidden; }
  body {
    background: var(--stage);
    font-family: "Lato", Arial, sans-serif;
    position: relative;
  }
  .card {
    position: absolute;
    width: 560px;
    height: 320px;
    border-radius: 22px;
    background: linear-gradient(160deg, #ffffff 0%, var(--card) 60%, var(--card-edge) 100%);
    overflow: hidden;
    box-shadow: 0 18px 40px rgba(0,0,0,.55);
  }
  .card--front { left: 60px; top: 80px; }
  .card--back { left: 580px; top: 470px; }

  /* brand name */
  .brand {
    position: absolute;
    display: flex;
    align-items: center;
    gap: 8px;
    color: var(--ink);
    font-weight: 900;
    white-space: nowrap;
  }
  .brand__dot {
    width: 16px; height: 16px;
    border-radius: 50%;
    background: var(--band-dark);
    flex: none;
  }
  .card--front .brand { left: 22px; top: 120px; font-size: 20px; }
  .card--back .brand { left: 34px; top: 108px; font-size: 28px; }

  /* front */
  .tow-photo {
    position: absolute;
    left: 240px; top: 34px;
    width: 296px; height: 180px;
    border-radius: 8px;
    background:
      radial-gradient(ellipse at 65% 40%, #c8242a 0%, rgba(200,36,42,.6) 28%, transparent 55%),
      radial-gradient(ellipse at 30% 70%, #2a2d33 0%, rgba(42,45,51,.5) 35%, transparent 60%),
      linear-gradient(180deg, #f2f2f2, #d9d9d9);
  }
  .front-band {
    position: absolute;
    left: 0; right: 0; bottom: 34px;
    height: 40px;
    border-top: 4px solid var(--rule);
    background: linear-gradient(180deg, var(--band-light), var(--band-mid) 55%, var(--band-dark));
    display: flex; align-items: center; justify-content: center;
  }
  .front-band__text {
    color: var(--accent);
    font-weight: 700;
    font-size: 15px;
    letter-spacing: 7px;
  }
  .front-base {
    position: absolute;
    left: 0; right: 0; bottom: 0;
    height: 22px;
    border-top: 3px solid var(--rule);
    background: linear-gradient(180deg, #f0f0f0, var(--band-mid));
  }

  /* back */
  .divider {
    position: absolute;
    left: 300px; top: 40px;
    width: 2px; height: 170px;
    background: var(--ink-soft);
  }
  .person { position: absolute; left: 330px; top: 40px; }
  .person__name {
    font-family: "Cinzel", Georgia, serif;
    font-size: 19px;
    font-weight: 500;
    color: var(--ink);
    letter-spacing: 1px;
  }
  .person__role {
    font-size: 9px;
    font-weight: 700;
    letter-spacing: .5px;
    color: var(--ink);
    margin-left: 26px;
  }
  .contacts {
    position: absolute;
    left: 318px; top: 104px;
    list-style: none;
    font-size: 14px;
    color: var(--ink-soft);
    line-height: 1.25;
  }
  .contacts li { display: flex; align-items: flex-start; gap: 6px; margin-bottom: 4px; }
  .contacts .icon { flex: none; margin-top: 1px; }
  .tab {
    position: absolute;
    right: 70px; bottom: 92px;
    background: var(--rule);
    color: var(--accent);
    font-weight: 700;
    font-size: 14px;
    padding: 4px 16px 3px;
    border-radius: 6px 6px 0 0;
  }
  .service-band {
    position: absolute;
    left: 0; right: 0; bottom: 36px;
    height: 56px;
    border-top: 4px solid var(--rule);
    background: linear-gradient(180deg, var(--band-light), var(--band-mid) 50%, var(--band-dark));
    display: flex; align-items: center; justify-content: center;
  }
  .services {
    list-style: none;
    display: flex; justify-content: center;
    white-space: nowrap;
    color: var(--accent);
    font-weight: 700;
    font-size: 14.5px;
    line-height: 1.4;
  }
  .services li + li::before { content: "•"; margin: 0 7px; color: var(--card); }
  .back-base {
    position: absolute;
    left: 0; right: 0; bottom: 0;
    height: 36px;
    border-top: 3px solid var(--rule);
    background: linear-gradient(180deg, #f4f4f4, #dcdcdc);
  }
</style>
</head>
<body>

<section class="card card--front" aria-label="Business card front">
  <div class="brand"><span class="brand__dot"></span>K &amp; M Tire Shop</div>
  <div class="tow-photo" role="img" aria-label="Photo of a red flatbed tow truck carrying a dark car"></div>
  <div class="front-band"><span class="front-band__text">WE OFFER FREE TOWING</span></div>
  <div class="front-base"></div>
</section>

<section class="card card--back" aria-label="Business card back">
  <div class="brand"><span class="brand__dot"></span>K &amp; M Tire Shop</div>
  <div class="divider"></div>
  <div class="person">
    <p class="person__name">DANA WHITFIELD</p>
    <p class="person__role">OWNER / FOUNDER</p>
  </div>
  <ul class="contacts">
    <li>
      <svg class="icon" width="16" height="16" viewBox="0 0 16 16" aria-hidden="true"><rect width="16" height="16" rx="3" fill="#111"/><rect x="5" y="3" width="6" height="10" rx="1" fill="#e6de2a"/></svg>
      (813) 572-6148
    </li>
    <li>
      <svg class="icon" width="16" height="16" viewBox="0 0 16 16" aria-hidden="true"><rect width="16" height="16" rx="3" fill="#111"/><rect x="3" y="5" width="10" height="7" fill="#e6de2a"/><path d="M3 5l5 4 5-4" stroke="#111" stroke-width="1" fill="none"/></svg>
      dana@kmtireshop.example
    </li>
    <li>
      <svg class="icon" width="16" height="16" viewBox="0 0 16 16" aria-hidden="true"><rect width="16" height="16" rx="3" fill="#111"/><path d="M8 3a3.5 3.5 0 0 1 3.5 3.5C11.5 9 8 13 8 13S4.5 9 4.5 6.5A3.5 3.5 0 0 1 8 3z" fill="#e6de2a"/><circle cx="8" cy="6.5" r="1.3" fill="#111"/></svg>
      <span>4187 N Crestwell Ave<br>Tampa, Fl 33829</span>
    </li>
  </ul>
  <div class="tab">Complete Auto Care</div>
  <div class="service-band">
    <ul class="services">
      <li>Brakes</li>
      <li>A/C Repair</li>
      <li>Engine tune-up</li>
      <li>Oil change</li>
      <li>Vehicle maintenance</li>
    </ul>
  </div>
  <div class="back-base"></div>
</section>

</body>
</html>
```